Three diagrams for research framework required

I need a three diagrams produced to capture principles of a research approach.<br/><br/>The first is a cycle diagram, produced to capture seven principles of a research framework. My idea is to be similar to the example attached, but incorporate seven principles and the koru (fern) imagery (example attached) that relates to our logo (also attached). The centre piece of the diagram should be labelled Open Meadow Wordcraft Method.<br/><br/>The seven principles are:<br/>1. Thinking proactively<br/>2. Ensuring positive learning experiences<br/>3. Fostering positive collaborations<br/>4. Providing constructive reporting<br/>5. Prioritising whānau engagement<br/>6. Being culturally responsive<br/>7. Maximizing protective factors<br/><br/>The second and third diagram should be updated versions of the attached, so all three diagrams look related. See diagrams attached that require updating (diagram 2 and 3).<br/><br/>The three diagrams need to be cohesive and clearly related aesthetically. All final files need to be produced in Adobe Photoshop or InDesign, so minor edits to text can easily be made in future.

Industry/Entity Type

Education

Font styles to use
Sans Serif

Colors

Designer to choose colors to be used in the design.

Requirements
Must have
• Clean design, easy to read and understand.
Should not have
• Complicated, overly busy design.

```html
<!DOCTYPE html>
<html lang="en">
<head>
<meta charset="utf-8">
<title>7 Principles of a Research Framework</title>
<link rel="stylesheet" href="https://fonts.googleapis.com/css2?family=Open+Sans:wght@300;400;700;800&family=Roboto+Condensed:wght@300;400;700&display=swap">
<style>
  :root {
    --meadow: #7cb041;
    --meadow-deep: #5d8a2f;
    --paper: #ffffff;
    --wine: #6b0f35;
    --orange: #f58823;
    --salmon: #f26f63;
    --slate: #546e7a;
    --aqua: #5ec8d6;
    --violet: #946db0;
    --azure: #0f76bc;
    --clay: #ab7c53;
  }
  html, body {
    margin: 0;
    padding: 0;
    width: 1200px;
    height: 848px;
    overflow: hidden;
    background: var(--meadow);
  }
  .poster { display: block; width: 1200px; height: 848px; }
  .bg-meadow { fill: var(--meadow); }
  .bg-paper { fill: var(--paper); }
  .ring-outer { fill: var(--meadow-deep); }
  .ring-inner { fill: var(--paper); }
  .hub { fill: var(--meadow); }

  .petal--01 { fill: var(--orange); }
  .petal--02 { fill: var(--salmon); }
  .petal--03 { fill: var(--slate); }
  .petal--04 { fill: var(--aqua); }
  .petal--05 { fill: var(--violet); }
  .petal--06 { fill: var(--azure); }
  .petal--07 { fill: var(--clay); }

  .num {
    font-family: "Roboto Condensed", sans-serif;
    font-weight: 700;
    font-size: 96px;
    fill: var(--paper);
    text-anchor: middle;
    letter-spacing: -4px;
  }
  .label {
    font-family: "Roboto Condensed", sans-serif;
    font-size: 46px;
    fill: var(--paper);
    text-anchor: middle;
  }
  .label .strong { font-weight: 700; }
  .label .light { font-weight: 400; }
  .is-wine { fill: var(--wine); }

  .icon-line { fill: none; stroke: var(--paper); stroke-width: 9; stroke-linecap: round; stroke-linejoin: round; }
  .icon-fill { fill: var(--paper); }
  .icon-wine { fill: none; stroke: var(--wine); stroke-width: 12; stroke-linecap: round; stroke-linejoin: round; }
  .icon-wine-fill { fill: var(--wine); }

  .hub-seven {
    font-family: "Open Sans", sans-serif;
    font-weight: 800;
    font-size: 300px;
    fill: var(--paper);
    text-anchor: middle;
  }
  .hub-title {
    font-family: "Open Sans", sans-serif;
    font-weight: 800;
    font-size: 64px;
    fill: var(--paper);
    text-anchor: middle;
  }
  .hub-sub {
    font-family: "Open Sans", sans-serif;
    font-weight: 400;
    font-size: 46px;
    fill: var(--paper);
    text-anchor: middle;
    letter-spacing: -1px;
  }

  .brand-mark { fill: var(--meadow); }
  .brand-name {
    font-family: "Open Sans", sans-serif;
    font-weight: 700;
    font-size: 52px;
    fill: var(--wine);
    text-anchor: middle;
  }

  .headline { text-anchor: middle; font-family: "Open Sans", sans-serif; }
  .headline--seven { font-weight: 800; font-size: 400px; }
  .headline--title { font-weight: 800; font-size: 98px; letter-spacing: -2px; }
  .headline--sub { font-weight: 400; font-size: 86px; letter-spacing: -4px; }
  .shadow { fill: var(--wine); }
  .face { fill: var(--paper); }
</style>
</head>
<body>
<svg class="poster" viewBox="0 0 2296 1623" xmlns="http://www.w3.org/2000/svg" role="img" aria-label="Seven principles of a research framework">
  <!-- backdrop -->
  <rect class="bg-meadow" x="0" y="0" width="2296" height="1623"/>
  <rect class="bg-paper" x="0" y="127" width="1100" height="533"/>

  <!-- wheel frame -->
  <circle class="ring-outer" cx="1590" cy="828" r="922"/>
  <circle class="ring-inner" cx="1590" cy="828" r="878"/>

  <!-- petals -->
  <g class="petals">
    <g class="petal petal--07">
      <path d="M1110,395 Q1300,250 1590,180 Q1690,360 1585,545 Q1460,560 1390,625 Q1300,440 1110,395 Z"/>
      <circle cx="1347" cy="218" r="95"/>
    </g>
    <g class="petal petal--01">
      <path d="M1630,180 Q1900,200 2095,420 Q1990,600 1810,645 Q1720,560 1625,545 Q1720,380 1630,180 Z"/>
      <circle cx="1775" cy="205" r="95"/>
    </g>
    <g class="petal petal--02">
      <path d="M2120,455 Q2270,650 2225,970 Q2030,1020 1870,885 Q1890,740 1835,680 Q2040,620 2120,455 Z"/>
      <circle cx="2180" cy="595" r="90"/>
    </g>
    <g class="petal petal--03">
      <path d="M1715,1080 Q1820,1010 1855,925 Q2000,1040 2210,1010 Q2080,1260 1880,1410 Q1680,1280 1715,1080 Z"/>
      <circle cx="2175" cy="1130" r="92"/>
    </g>
    <g class="petal petal--04">
      <path d="M1470,1085 Q1580,1110 1680,1100 Q1680,1300 1835,1425 Q1600,1510 1310,1410 Q1300,1220 1470,1085 Z"/>
      <circle cx="1557" cy="1462" r="92"/>
    </g>
    <g class="petal petal--05">
      <path d="M960,975 Q1120,860 1315,895 Q1350,1010 1435,1065 Q1280,1180 1275,1390 Q1120,1300 1030,1160 Z"/>
      <circle cx="980" cy="1095" r="95"/>
    </g>
    <g class="petal petal--06">
      <path d="M1080,425 Q1280,460 1365,655 Q1300,740 1308,855 Q1110,820 950,930 Q920,780 975,630 Z"/>
      <circle cx="1005" cy="540" r="95"/>
    </g>
  </g>

  <!-- icons -->
  <g class="icons">
    <!-- shield -->
    <path class="icon-line" d="M1450,272 Q1480,292 1497,290 L1497,330 Q1494,365 1450,380 Q1406,365 1403,330 L1403,290 Q1420,292 1450,272 Z"/>
    <path class="icon-line" d="M1450,295 Q1470,307 1480,306 L1480,330 Q1477,352 1450,362 Q1423,352 1420,330 L1420,306 Q1430,307 1450,295 Z" stroke-width="5"/>
    <!-- light bulb -->
    <g class="icon-line">
      <circle cx="1852" cy="370" r="30"/>
      <path d="M1840,400 L1840,418 L1864,418 L1864,400"/>
      <line x1="1842" y1="428" x2="1862" y2="428"/>
      <line x1="1852" y1="318" x2="1852" y2="330"/>
      <line x1="1802" y1="365" x2="1815" y2="365"/>
      <line x1="1889" y1="365" x2="1902" y2="365"/>
      <line x1="1818" y1="330" x2="1827" y2="339"/>
      <line x1="1886" y1="330" x2="1877" y2="339"/>
    </g>
    <!-- open book -->
    <g class="icon-line">
      <path d="M2062,765 L2062,700 Q2040,690 2015,695 L2015,765 Q2040,758 2062,765 Z"/>
      <path d="M2062,765 L2062,700 Q2084,690 2110,695 L2110,765 Q2084,758 2062,765 Z"/>
      <line x1="2062" y1="680" x2="2062" y2="722"/>
      <line x1="2047" y1="695" x2="2077" y2="695"/>
    </g>
    <!-- puzzle -->
    <g>
      <rect class="icon-fill" x="1873" y="1040" width="100" height="100"/>
      <path d="M1923,1040 L1923,1140 M1873,1090 L1973,1090" stroke="var(--slate)" stroke-width="5"/>
      <circle cx="1923" cy="1070" r="8" fill="none" stroke="var(--slate)" stroke-width="5"/>
      <circle cx="1943" cy="1090" r="8" fill="none" stroke="var(--slate)" stroke-width="5"/>
      <circle cx="1903" cy="1090" r="8" fill="none" stroke="var(--slate)" stroke-width="5"/>
      <circle cx="1923" cy="1112" r="8" fill="none" stroke="var(--slate)" stroke-width="5"/>
    </g>
    <!-- document with tick -->
    <g>
      <path class="icon-wine" d="M1510,1195 L1565,1195 L1585,1215 L1585,1272 L1510,1272 Z"/>
      <line class="icon-wine" x1="1527" y1="1230" x2="1568" y2="1230" stroke-width="8"/>
      <line class="icon-wine" x1="1527" y1="1246" x2="1568" y2="1246" stroke-width="8"/>
      <line class="icon-wine" x1="1527" y1="1260" x2="1568" y2="1260" stroke-width="8"/>
      <path class="icon-wine" d="M1500,1180 L1520,1197 L1562,1155"/>
    </g>
    <!-- network -->
    <g>
      <g class="icon-line">
        <line x1="1190" y1="1000" x2="1177" y2="940"/>
        <line x1="1190" y1="1000" x2="1222" y2="950"/>
        <line x1="1190" y1="1000" x2="1130" y2="1012"/>
        <line x1="1190" y1="1000" x2="1248" y2="1035"/>
        <circle cx="1190" cy="1000" r="18"/>
      </g>
      <circle class="icon-fill" cx="1177" cy="938" r="16"/>
      <circle class="icon-fill" cx="1222" cy="948" r="12"/>
      <circle class="icon-fill" cx="1128" cy="1013" r="16"/>
      <circle class="icon-fill" cx="1248" cy="1035" r="16"/>
    </g>
    <!-- group of people -->
    <g class="icon-fill">
      <circle cx="1107" cy="563" r="18"/>
      <circle cx="1171" cy="563" r="18"/>
      <path d="M1075,630 Q1075,590 1107,590 Q1130,590 1135,605 L1110,635 Z"/>
      <path d="M1203,630 Q1203,590 1171,590 Q1148,590 1143,605 L1168,635 Z"/>
      <circle cx="1139" cy="583" r="20" stroke="var(--azure)" stroke-width="6"/>
      <path d="M1105,645 Q1105,605 1139,605 Q1173,605 1173,645 Q1139,660 1105,645 Z" stroke="var(--azure)" stroke-width="6"/>
    </g>
  </g>

  <!-- numbers -->
  <g class="numbers">
    <text class="num" x="1347" y="243">07</text>
    <text class="num" x="1770" y="233">01</text>
    <text class="num" x="2185" y="628">02</text>
    <text class="num" x="2150" y="1162">03</text>
    <text class="num is-wine" x="1555" y="1505">04</text>
    <text class="num" x="980" y="1128">05</text>
    <text class="num" x="1003" y="572">06</text>
  </g>

  <!-- labels -->
  <g class="labels">
    <text class="label" x="1447" y="440"><tspan class="strong">Maximizing</tspan><tspan class="strong" x="1447" dy="42">Protective</tspan><tspan class="light" x="1447" dy="42">Factors</tspan></text>
    <text class="label" x="1848" y="487"><tspan class="strong">Thinking</tspan><tspan class="light" x="1848" dy="58">Proactively</tspan></text>
    <text class="label" x="2062" y="832"><tspan class="strong">Ensuring Positive</tspan><tspan class="light" x="2062" dy="42">Learning</tspan><tspan class="light" x="2062" dy="42">Experiences</tspan></text>
    <text class="label" x="1922" y="1198"><tspan class="strong">Fostering Positive</tspan><tspan class="light" x="1922" dy="42">collaborations</tspan></text>
    <text class="label is-wine" x="1543" y="1338"><tspan class="light">Providing</tspan><tspan class="strong" x="1543" dy="44">Constructive Reporting</tspan></text>
    <text class="label" x="1190" y="1112"><tspan class="strong">Prioritising</tspan><tspan class="strong" x="1190" dy="42">Whānau</tspan><tspan class="light" x="1190" dy="42">Engagement</tspan></text>
    <text class="label" x="1132" y="712"><tspan class="light">Being</tspan><tspan class="strong" x="1132" dy="42">Culturally</tspan><tspan class="strong" x="1132" dy="42">Responsive</tspan></text>
  </g>

  <!-- hub -->
  <circle class="hub" cx="1592" cy="827" r="255"/>
  <text class="hub-seven" x="1592" y="808">7</text>
  <text class="hub-title" x="1592" y="893">PRINCIPLES</text>
  <text class="hub-sub" x="1592" y="948">OF A RESEARCH</text>
  <text class="hub-sub" x="1592" y="1003">FRAMEWORK</text>

  <!-- brand lockup -->
  <circle class="brand-mark" cx="368" cy="318" r="110"/>
  <text class="brand-name" x="363" y="508">Open Meadow</text>
  <text class="brand-name" x="363" y="570">Wordcraft Method</text>

  <!-- headline -->
  <g class="headline">
    <text class="headline--seven shadow" x="410" y="1192">7</text>
    <text class="headline--seven face" x="400" y="1186">7</text>
    <text class="headline--title shadow" x="406" y="1326">PRINCIPLES</text>
    <text class="headline--title face" x="400" y="1320">PRINCIPLES</text>
    <text class="headline--sub shadow" x="404" y="1420">OF A RESEARCH</text>
    <text class="headline--sub face" x="398" y="1415">OF A RESEARCH</text>
    <text class="headline--sub shadow" x="404" y="1515">FRAMEWORK</text>
    <text class="headline--sub face" x="398" y="1510">FRAMEWORK</text>
  </g>
</svg>
</body>
</html>
```